Harwell Systems Advisory - IT Consultancy

I already have a Wordpress site, but not happy with the look and feel or the template I chose.
I want a site as a web presence only, I can configure base SEO myself, but most business is referrals not from a search, so low priority.

My current site is http://harsysadv.example where you can see the sort of content I already have.

Target Market(s)

Business to Business services.

Industry/Entity Type

Consulting

Font styles to use
Sans Serif

Colors
3277b5

Requirements
Must have
• Front Page Template
• Freephone number on front page.
• My Logo and the Venturix logo on the front page
• Page template for Services, Solutions and Portfolio
• Contact Page
• Ability to embed links to Video clips hosted by a third party
Nice to have
• Each page could have a side bar with some common functions, like Request Demo.
• Second Contact Page specifically to Request Demonstrations of Venturix Products, the demo contact page needs to capture some additional information in text boxes and also a check box list of features. The list of features needs to be easily configurable.
• Features to include in checkbox list.
• Contract Management
• Service Desk
• Document Management
• Contract Management
• Business Workflow

```html
<!DOCTYPE html>
<html lang="en">
<head>
<meta charset="utf-8">
<title>Harwell Systems Advisory – IT Consultancy</title>
<link href="https://fonts.googleapis.com/css2?family=Open+Sans:ital,wght@0,300;0,400;0,600;0,700;1,400&display=swap" rel="stylesheet">
<style>
:root{
  --blue:#3277b5;
  --blue-bright:#1f8ad6;
  --blue-dark:#1d4f86;
  --ink:#333;
  --muted:#777;
  --line:#dcdcdc;
  --panel:#f1f2f4;
  --clients:#474747;
  --footer:#2e2e2e;
  --copy:#222;
  --white:#fff;
}
*{box-sizing:border-box;margin:0;padding:0}
html,body{width:1200px;height:2668px;overflow:hidden}
body{font-family:"Open Sans",Arial,sans-serif;color:var(--ink);background:var(--white);font-size:13px}
.topbar{height:36px;border-bottom:1px solid var(--line);display:flex;align-items:center;justify-content:space-between;padding:0 130px;font-size:11px;color:var(--muted)}
.topbar .contact{display:flex;gap:26px;align-items:center}
.topbar .contact span{display:flex;align-items:center;gap:6px}
.topbar .right{display:flex;align-items:center;gap:24px}
.social{display:flex;gap:6px}
.social i{width:18px;height:18px;border-radius:50%;background:var(--blue-bright);display:block}
.search{width:130px;height:22px;border:1px solid var(--line);display:flex;align-items:center;justify-content:space-between;padding:0 8px;color:#aaa}
.header{height:64px;display:flex;align-items:center;justify-content:space-between;padding:0 130px}
.logo .name{font-size:30px;font-weight:700;color:var(--blue);letter-spacing:2px;line-height:1}
.logo .sub{font-size:10.5px;color:var(--blue);letter-spacing:1.6px;margin-top:2px}
.nav{display:flex;gap:34px;font-size:11px;font-weight:600;color:#555}
.nav a{color:inherit;text-decoration:none;padding:6px 8px}
.nav a.active{border:1px solid var(--blue);color:var(--blue)}
.hero{height:530px;position:relative;background:radial-gradient(ellipse at 55% 40%,#6fb3ea 0%,#2d74b7 45%,#0f2f5c 100%)}
.hero .caption{position:absolute;left:0;right:0;bottom:30px;height:44px;background:rgba(10,35,70,.55);display:flex;align-items:center;justify-content:center;color:var(--white);font-weight:600;font-size:15px;letter-spacing:.5px}
.services{height:430px;padding-top:34px;text-align:center}
.section-title{font-size:30px;font-weight:300;color:#444}
.section-title b{font-weight:400;color:var(--blue)}
.service-row{display:flex;justify-content:center;gap:42px;margin-top:46px}
.service{width:150px}
.service .icon{width:72px;height:72px;margin:0 auto}
.service h3{font-size:14px;font-weight:400;color:#444;margin-top:14px;line-height:1.3}
.service p{font-size:10px;color:var(--muted);line-height:1.5;margin-top:12px}
.btn-small{display:inline-block;margin-top:14px;border:1px solid var(--blue);color:var(--blue);font-size:9px;padding:2px 8px;border-radius:2px}
.welcome{height:330px;background:var(--panel);display:flex;padding:32px 130px 0}
.welcome .intro{width:540px;padding-right:40px;border-right:1px solid #cfd3d8;height:250px}
.welcome h2{font-size:26px;font-weight:400;color:#444;line-height:1.2}
.welcome h2 span{display:block;color:var(--blue);font-size:24px}
.welcome .lead{font-size:10.5px;color:#555;line-height:1.6;margin-top:14px}
.pillars{display:flex;gap:30px;margin-top:22px}
.pillar{display:flex;gap:10px;width:220px}
.pillar svg{flex:none}
.pillar h4{font-size:13px;font-weight:600;color:var(--blue)}
.pillar p{font-size:9.5px;color:var(--muted);line-height:1.5;margin-top:4px}
.partner{flex:1;display:flex;align-items:center;justify-content:center;padding-bottom:60px}
.partner-mark{display:flex;align-items:center;gap:14px;font-size:46px;font-weight:700;color:var(--blue-dark)}
.partner-mark i{width:30px;height:30px;background:#e8812e;display:block}
.testimonials{height:310px;position:relative;background:linear-gradient(180deg,#1e5fa3 0%,#3c8ad0 55%,#2a6db2 100%)}
.testimonials h2{position:absolute;top:26px;width:100%;text-align:center;color:var(--white);font-size:26px;font-weight:300}
.quote-card{position:absolute;left:100px;right:100px;top:84px;height:190px;background:var(--white);border-radius:6px;display:flex;align-items:center;padding:0 40px;gap:36px}
.client-badge{display:flex;align-items:center;gap:8px;font-size:20px;font-weight:700;color:#e8812e;width:160px}
.client-badge i{width:22px;height:22px;border-radius:50%;background:#e8812e;display:block}
.quote{flex:1;font-size:10.5px;color:#555;line-height:1.65}
.quote .more{color:var(--blue);font-style:italic}
.author{display:flex;align-items:center;gap:12px;align-self:flex-end;margin-bottom:22px}
.author .sig{font-size:17px;font-style:italic;color:#222}
.author .photo{width:52px;height:60px;background:linear-gradient(#8a9099,#4d535b)}
.news{height:480px;display:flex;gap:50px;padding:36px 130px 0}
.news .col{flex:1}
.col-head{display:flex;justify-content:space-between;align-items:baseline;border-bottom:1px solid var(--line);padding-bottom:8px}
.col-head h2{font-size:20px;font-weight:400;color:#444}
.col-head h2 b{font-weight:400;color:var(--blue)}
.col-head a{font-size:10px;color:var(--blue);text-decoration:none}
.news-item{display:flex;gap:14px;margin-top:24px}
.date{width:58px;height:64px;background:var(--blue-bright);color:var(--white);text-align:center;flex:none;padding-top:6px}
.date b{display:block;font-size:22px;line-height:1}
.date span{display:block;font-size:10px;line-height:1.3}
.news-item h4{font-size:11px;font-weight:600;color:#444}
.news-item p{font-size:9.5px;color:var(--muted);line-height:1.55;margin-top:4px}
.blog-item{display:flex;gap:16px;margin-top:22px;align-items:flex-start}
.blog-item .thumb{width:62px;height:62px;border-radius:50%;background:linear-gradient(#b9c3cf,#6d7b8c);flex:none}
.blog-item p{font-size:9.5px;color:#555;line-height:1.55}
.blog-item h4{font-size:11px;font-weight:600;color:var(--blue);margin-top:4px;border-bottom:1px solid var(--line);padding-bottom:6px}
.clients{height:150px;background:var(--clients);display:flex;align-items:center;padding:0 130px;gap:40px}
.clients h2{color:var(--white);font-size:24px;font-weight:300;line-height:1.1;width:110px}
.client-row{display:flex;align-items:center;gap:18px;flex:1}
.client-row .arrow{color:#aaa;font-size:20px}
.client-logo{flex:1;height:52px;background:var(--white);border-radius:3px;display:flex;align-items:center;justify-content:center;font-weight:700;font-size:14px;color:var(--blue)}
.newsletter{height:60px;background:var(--blue-bright);display:flex;align-items:center;justify-content:center;gap:24px;color:var(--white)}
.newsletter h3{font-size:16px;font-weight:400}
.newsletter .field{width:320px;height:30px;background:var(--white);color:#999;font-size:11px;padding:0 10px;display:flex;align-items:center}
.newsletter .btn{height:30px;background:var(--blue-dark);padding:0 22px;display:flex;align-items:center;font-size:12px}
.footer{height:250px;background:var(--footer);display:flex;padding:30px 130px 0;gap:50px;color:#bbb;position:relative}
.footer h4{color:var(--white);font-size:13px;font-weight:400;border-bottom:1px solid #555;padding-bottom:8px;margin-bottom:10px}
.quick{width:150px}
.quick li{list-style:none;font-size:10px;line-height:2.3}
.quick li::before{content:"› ";color:var(--blue-bright)}
.contact-col{width:250px;font-size:10px;line-height:1.8}
.contact-col .row{display:flex;gap:8px;align-items:center}
.map{width:160px;height:130px;margin-top:34px;background:linear-gradient(135deg,#d9dcdf,#b8bec4)}
.footer .mark{position:absolute;right:130px;top:40px;font-size:60px;font-weight:700;letter-spacing:6px;color:#3c3c3c}
.copyright{height:28px;background:var(--copy);color:#888;font-size:9.5px;display:flex;align-items:center;justify-content:center}
</style>
</head>
<body>

<div class="topbar">
  <div class="contact">
    <span><svg width="10" height="10" viewBox="0 0 10 10"><path d="M2 1l2 2-1 1.3a6 6 0 0 0 2.7 2.7L7 6l2 2-1.3 1.5C4.5 9.2.8 5.5.5 2.3z" fill="#3277b5"/></svg>+44 (0)800 612 4470</span>
    <span><svg width="12" height="9" viewBox="0 0 12 9"><rect x=".5" y=".5" width="11" height="8" fill="none" stroke="#3277b5"/><path d="M.5.5 6 5l5.5-4.5" fill="none" stroke="#3277b5"/></svg>info@harsysadv.example</span>
  </div>
  <div class="right">
    <div class="social"><i></i><i></i><i></i><i></i></div>
    <div class="search">Search <svg width="10" height="10" viewBox="0 0 10 10"><circle cx="4" cy="4" r="3" fill="none" stroke="#999"/><path d="M6.3 6.3 9 9" stroke="#999"/></svg></div>
  </div>
</div>

<header class="header">
  <div class="logo"><div class="name">HARWELL</div><div class="sub">SYSTEMS ADVISORY</div></div>
  <nav class="nav"><a class="active">HOME</a><a>SERVICE</a><a>SOLUTIONS</a><a>PORTFOLIO</a><a>CONTACT US</a></nav>
</header>

<section class="hero" role="img" aria-label="Hand touching a glowing network of connected business technology icons">
  <div class="caption">LOREM IPSUM DOLOR SIT AMET, CONSECTETUR ADIPISCING ELIT SED DIAM NONUMMY</div>
</section>

<section class="services">
  <h2 class="section-title">Our Business <b>Services</b></h2>
  <div class="service-row">
    <div class="service">
      <svg class="icon" viewBox="0 0 72 72"><circle cx="36" cy="36" r="34" fill="none" stroke="#cfe0f0" stroke-width="3"/><path d="M36 2a34 34 0 0 1 34 34" fill="none" stroke="#3277b5" stroke-width="3"/><circle cx="36" cy="36" r="27" fill="#3277b5"/><rect x="26" y="24" width="20" height="25" fill="none" stroke="#fff" stroke-width="2"/><path d="M30 31h12M30 36h12M30 41h8" stroke="#fff" stroke-width="2"/></svg>
      <h3>Project<br>Management</h3><p>Lorem ipsum dolor sit amet consectetur adipiscing elit sed do eiusmod.</p><span class="btn-small">Read More</span>
    </div>
    <div class="service">
      <svg class="icon" viewBox="0 0 72 72"><circle cx="36" cy="36" r="34" fill="none" stroke="#cfe0f0" stroke-width="3"/><path d="M36 2a34 34 0 0 1 34 34" fill="none" stroke="#3277b5" stroke-width="3"/><circle cx="36" cy="36" r="27" fill="#3277b5"/><rect x="26" y="23" width="20" height="26" fill="none" stroke="#fff" stroke-width="2"/><path d="M30 42l4 3 7-9" fill="none" stroke="#fff" stroke-width="2"/></svg>
      <h3>Contract<br>Management</h3><p>Lorem ipsum dolor sit amet consectetur adipiscing elit sed do eiusmod.</p><span class="btn-small">Read More</span>
    </div>
    <div class="service">
      <svg class="icon" viewBox="0 0 72 72"><circle cx="36" cy="36" r="34" fill="none" stroke="#cfe0f0" stroke-width="3"/><path d="M36 2a34 34 0 0 1 34 34" fill="none" stroke="#3277b5" stroke-width="3"/><circle cx="36" cy="36" r="27" fill="#3277b5"/><path d="M25 38v-3a11 11 0 0 1 22 0v3" fill="none" stroke="#fff" stroke-width="2"/><rect x="23" y="37" width="6" height="9" fill="#fff"/><rect x="43" y="37" width="6" height="9" fill="#fff"/></svg>
      <h3>Service<br>Desk</h3><p>Lorem ipsum dolor sit amet consectetur adipiscing elit sed do eiusmod.</p><span class="btn-small">Read More</span>
    </div>
    <div class="service">
      <svg class="icon" viewBox="0 0 72 72"><circle cx="36" cy="36" r="34" fill="none" stroke="#cfe0f0" stroke-width="3"/><path d="M36 2a34 34 0 0 1 34 34" fill="none" stroke="#3277b5" stroke-width="3"/><circle cx="36" cy="36" r="27" fill="#3277b5"/><path d="M24 28h9l3 3h12v17H24z" fill="none" stroke="#fff" stroke-width="2"/></svg>
      <h3>Document<br>Management</h3><p>Lorem ipsum dolor sit amet consectetur adipiscing elit sed do eiusmod.</p><span class="btn-small">Read More</span>
    </div>
    <div class="service">
      <svg class="icon" viewBox="0 0 72 72"><circle cx="36" cy="36" r="34" fill="none" stroke="#cfe0f0" stroke-width="3"/><path d="M36 2a34 34 0 0 1 34 34" fill="none" stroke="#3277b5" stroke-width="3"/><circle cx="36" cy="36" r="27" fill="#3277b5"/><rect x="23" y="25" width="10" height="8" fill="#fff"/><rect x="39" y="25" width="10" height="8" fill="#fff"/><rect x="31" y="41" width="10" height="8" fill="#fff"/><path d="M28 33v4h16v-4M36 37v4" fill="none" stroke="#fff" stroke-width="2"/></svg>
      <h3>Business<br>Workflow</h3><p>Lorem ipsum dolor sit amet consectetur adipiscing elit sed do eiusmod.</p><span class="btn-small">Read More</span>
    </div>
  </div>
</section>

<section class="welcome">
  <div class="intro">
    <h2>WELCOME TO<span>HARWELL SYSTEMS ADVISORY</span></h2>
    <p class="lead">Lorem ipsum dolor sit amet, consectetur adipiscing elit, sed diam nonummy nibh euismod tincidunt ut laoreet dolore magna aliquam erat volutpat. Ut wisi enim ad minim veniam, quis nostrud exerci tation ullamcorper suscipit lobortis nisl ut aliquip ex ea commodo consequat duis autem vel eum iriure dolor.</p>
    <div class="pillars">
      <div class="pillar">
        <svg width="40" height="40" viewBox="0 0 40 40"><circle cx="20" cy="20" r="19" fill="#3277b5"/><circle cx="20" cy="16" r="5" fill="#fff"/><path d="M11 29a9 7 0 0 1 18 0z" fill="#fff"/></svg>
        <div><h4>Who We Are</h4><p>Sed ut perspiciatis unde omnis iste natus error sit voluptatem accusantium.</p></div>
      </div>
      <div class="pillar">
        <svg width="40" height="40" viewBox="0 0 40 40"><circle cx="20" cy="20" r="19" fill="#3277b5"/><path d="M8 20s5-7 12-7 12 7 12 7-5 7-12 7S8 20 8 20z" fill="#fff"/><circle cx="20" cy="20" r="3.5" fill="#3277b5"/></svg>
        <div><h4>Our Vision</h4><p>Sed ut perspiciatis unde omnis iste natus error sit voluptatem accusantium.</p></div>
      </div>
    </div>
  </div>
  <div class="partner">
    <div class="partner-mark"><i></i>Venturix</div>
  </div>
</section>

<section class="testimonials" role="img" aria-label="Blue world map backdrop with network lines">
  <h2>What Our Customer Say About Us</h2>
  <div class="quote-card">
    <div class="client-badge"><i></i>Norvane</div>
    <p class="quote">Lorem ipsum dolor sit amet, consectetur adipiscing elit. Integer venenatis tincidunt elit aliquam semper quam pulvinar ac. Aliquam erat volutpat integer varius eros ut pretium consectetur, mauris nisl vehicula justo, vel rhoncus lorem erat sed nulla. Integer varius eros ut pretium consectetur. Lorem ipsum dolor sit amet. <span class="more">...read more</span></p>
    <div class="author"><span class="sig">Dana Whitfield</span><div class="photo" role="img" aria-label="Portrait of the client"></div></div>
  </div>
</section>

<section class="news">
  <div class="col">
    <div class="col-head"><h2>Recent <b>News &amp; Events</b></h2><a>View All News →</a></div>
    <div class="news-item">
      <div class="date"><b>22</b><span>Feb<br>2016</span></div>
      <div><h4>Lorem Ipsum Dolor Consecte</h4><p>Lorem ipsum dolor sit amet consectetur adipiscing elit sed diam nonummy nibh euismod tincidunt ut laoreet dolore magna aliquam erat volutpat ut wisi enim ad minim veniam.</p><span class="btn-small">Read More</span></div>
    </div>
    <div class="news-item">
      <div class="date"><b>23</b><span>Feb<br>2016</span></div>
      <div><h4>Lorem Ipsum Dolor Consecte</h4><p>Lorem ipsum dolor sit amet consectetur adipiscing elit sed diam nonummy nibh euismod tincidunt ut laoreet dolore magna aliquam erat volutpat ut wisi enim ad minim veniam.</p><span class="btn-small">Read More</span></div>
    </div>
  </div>
  <div class="col">
    <div class="col-head"><h2>Latest <b>Blog Posts</b></h2><a>View All →</a></div>
    <div class="blog-item">
      <div class="thumb" role="img" aria-label="Author photo"></div>
      <div><p>Lorem ipsum dolor sit amet, consectetuer adipiscing elit, sed diam nonummy nibh euismod tincidunt ut laoreet dolore magna.</p><h4>Consectetur Adipiscing</h4></div>
    </div>
    <div class="blog-item">
      <div class="thumb" role="img" aria-label="Author photo"></div>
      <div><p>Lorem ipsum dolor sit amet, consectetuer adipiscing elit, sed diam nonummy nibh euismod tincidunt ut laoreet dolore magna.</p><h4>Diam Nonummy</h4></div>
    </div>
  </div>
</section>

<section class="clients">
  <h2>Our<br>Clients</h2>
  <div class="client-row">
    <span class="arrow">‹</span>
    <div class="client-logo">Norvane</div>
    <div class="client-logo">Kestrel Labs</div>
    <div class="client-logo">Brightmoor</div>
    <div class="client-logo">Tallis Group</div>
    <div class="client-logo">Orinda</div>
    <span class="arrow">›</span>
  </div>
</section>

<section class="newsletter">
  <h3>Subscribe to Our Newsletter</h3>
  <div class="field">Enter email address</div>
  <div class="btn">Subscribe</div>
</section>

<footer class="footer">
  <div class="quick">
    <h4>Quick Links</h4>
    <ul><li>HOME</li><li>SERVICE</li><li>SOLUTIONS</li><li>PORTFOLIO</li><li>CONTACT US</li></ul>
  </div>
  <div class="contact-col">
    <h4>Contact Us</h4>
    <p>Harwell Systems Advisory Ltd<br>14 Fenwick Lane, Oxford OX1 4QT</p>
    <div class="row">☎ +44 (0)800 612 4470</div>
    <div class="row">✉ info@harsysadv.example</div>
    <div class="row">⌂ http://harsysadv.example</div>
  </div>
  <div class="map" role="img" aria-label="Street map showing office location"></div>
  <div class="mark">HARWELL</div>
</footer>

<div class="copyright">Copyright © 2016 Harwell Systems Advisory Ltd. All Rights Reserved</div>

</body>
</html>
```